Computer Training in the Education sector - Letterhead

We need a new letter head to be designed for the company. We provide computer training fro the Education Sector, both primary and private tertiary providers. The colours will need to tie in with the website www.lanternpathlearning.co.nz.
The company name is Lantern Path Co with the tag line of Computer Training for Educators.
The footer will need to have the following detail...
0508 KEY MENTOR
027 813 459
www.lanternpathlearning.co.nz / lessons@lanternpathlearning.co.nz
Updates

Thanks for the designs so far.

Some have watermarks in the background. Please don't worry about using watermarks as I will not be using a watermark in in a final design.
Regards,
Morris

Thank you for all the designs and the effort. There was some great concepts that came through.

Cheers
Morris

Industry/Entity Type

Computer

```html
<!DOCTYPE html>
<html lang="en">
<head>
<meta charset="utf-8">
<title>Lantern Path Co – Letterhead</title>
<link rel="stylesheet" href="https://fonts.googleapis.com/css2?family=Open+Sans:wght@400;600;700&display=swap">
<style>
  :root {
    --backdrop: #e6e7e9;
    --paper: #ffffff;
    --brand-blue: #2f7fc1;
    --brand-orange: #f39a3c;
    --brand-green: #7cc243;
    --brand-cyan: #2fb3e6;
    --footer-ink: #1f1f1f;
  }
  html, body {
    margin: 0;
    padding: 0;
    width: 1200px;
    height: 900px;
    overflow: hidden;
    background: var(--backdrop);
  }
  .canvas {
    position: relative;
    width: 1200px;
    height: 900px;
    display: flex;
    align-items: center;
    justify-content: center;
  }
  .letterhead {
    position: relative;
    width: 608px;
    height: 860px;
    background: var(--paper);
    box-shadow: 0 2px 10px rgba(0,0,0,0.12);
    font-family: "Open Sans", Arial, sans-serif;
    overflow: hidden;
  }
  .brand {
    position: absolute;
    top: 22px;
    left: 0;
    right: 0;
    text-align: center;
  }
  .brand-mark {
    display: block;
    margin: 0 auto 10px;
    width: 74px;
    height: 74px;
    border-radius: 50%;
    background: var(--brand-blue);
  }
  .brand-name {
    margin: 0;
    font-size: 17px;
    font-weight: 600;
    letter-spacing: 0.2px;
    color: var(--brand-blue);
    line-height: 1.1;
  }
  .brand-tagline {
    margin: 2px 0 0;
    font-size: 8.5px;
    font-weight: 700;
    color: var(--brand-green);
  }
  .footer-wash {
    position: absolute;
    left: 0;
    right: 0;
    bottom: 0;
    height: 190px;
    background:
      radial-gradient(ellipse 42% 70% at 0% 100%, rgba(243,154,60,0.95), rgba(243,154,60,0) 100%),
      radial-gradient(ellipse 40% 75% at 50% 100%, rgba(47,179,230,0.9), rgba(47,179,230,0) 100%),
      radial-gradient(ellipse 45% 85% at 100% 100%, rgba(124,194,67,0.95), rgba(124,194,67,0) 100%);
  }
  .footer-wash::before {
    content: "";
    position: absolute;
    inset: 0;
    background: linear-gradient(to bottom, var(--paper) 0%, rgba(255,255,255,0) 55%);
  }
  .contact {
    position: absolute;
    left: 0;
    right: 0;
    bottom: 20px;
    text-align: center;
    font-size: 9.5px;
    line-height: 1.3;
    color: var(--footer-ink);
  }
  .contact p { margin: 0; }
</style>
</head>
<body>
  <main class="canvas">
    <article class="letterhead">
      <header class="brand">
        <span class="brand-mark" aria-hidden="true"></span>
        <p class="brand-name">LANTERN PATH CO</p>
        <p class="brand-tagline">Computer Training for Educators</p>
      </header>
      <div class="footer-wash" aria-hidden="true"></div>
      <footer class="contact">
        <p>0508 KEY MENTOR</p>
        <p>027 813 459</p>
        <p>www.lanternpathlearning.co.nz / lessons@lanternpathlearning.co.nz</p>
      </footer>
    </article>
  </main>
</body>
</html>
```